Price list for young Relaxon clinic

I require a price list/Treatment menu for clinic

To include:
Logo
Address
Phone number
Website

List of services and Prices
Relaxon 1 area £100
Relaxon 2 areas £150
Relaxon 3 areas £200
Lip Enhancement 0.5ml £100
Lip Enhancement 1ml £200
Facial Fillers £200 per 1ml
Volumiq £450 per session (2 vials - must be bought as a course)
Non Surgical Face Lift (Thread Lift) £600 per area
Skin Press Full Face £250
Skin Press Small Per Small Area £100
Cryo Therapy £60
Chemical Peel Light Peel and Microdermabrasion £85
Chemical Peel Deep Peel £150
Consultation £30 redeemable against service
Relaxon Top Up Relaxon £50 (must be within 2 weeks of 1st treatment)
Filler Top Up £100 (must be within 2 weeks of 1st appointment)

Open Hours
Updates

Company Name: HVM Address: 482 Pellbrook Road, 6 Warnford High Street, KT4 3JQ Phone: 0208 947 2186 Website: www.hollyvanmereaesthetics.co.uk

Please add more colour

Needs to be much cleaner and simpler Front page to include logo and price list Back page to inculde open hours and contact information including google map. Please no images with needles. Images of lips and faces are good, but try not to crowd copy on the pagei. No copy on top of images. White, grey, black and reds are good on colouring.

Target Market(s)

young market ages 22-45 years old mainly female
modern

Industry/Entity Type

Clinic

Number of Pages Required

4 page

Requirements
Must have
• Logo - logo must be in colour grey/silver
• Address (small map?)
• Phone number
• Web address
• Services
• Open hours
• Prices
• Images

```html
<!DOCTYPE html>
<html lang="en">
<head>
<meta charset="utf-8">
<title>HVM Treatment Menu</title>
<link href="https://fonts.googleapis.com/css2?family=Arimo:wght@400;700&display=swap" rel="stylesheet">
<style>
  :root {
    --backdrop: #e9e9e9;
    --paper: #ffffff;
    --band-grey: #9d9d9f;
    --logo-grey: #a3a3a5;
    --ink: #1b1b1b;
    --muted: #8a8a8a;
    --sky-top: #3f74b8;
    --sky-bottom: #a9c6e6;
    --skin-light: #f3e4dc;
    --skin-mid: #d9b8a6;
    --map-light: #e4e2dd;
    --map-mid: #cfcdc8;
  }
  * { box-sizing: border-box; margin: 0; padding: 0; }
  html, body {
    width: 1200px; height: 1000px; overflow: hidden;
    background: var(--backdrop);
    font-family: "Arimo", Arial, sans-serif;
    color: var(--ink);
  }
  .flyer {
    position: absolute; left: 268px; top: 30px;
    width: 664px; height: 940px;
    background: var(--paper);
    box-shadow: 0 2px 10px rgba(0,0,0,.18);
    overflow: hidden;
  }
  .brand {
    position: absolute; left: 0; top: 0; width: 340px; height: 215px;
    text-align: center; color: var(--logo-grey);
  }
  .brand__initials {
    display: block; margin-top: 46px;
    font-size: 50px; letter-spacing: 6px; font-weight: 400;
  }
  .brand__name {
    display: block; margin-top: 18px;
    font-size: 22px; letter-spacing: 5px; line-height: 1.25; font-weight: 400;
  }
  .brand__web {
    position: absolute; left: 26px; top: 192px;
    font-size: 14px; color: var(--ink);
  }
  .contact-band {
    position: absolute; left: 0; top: 215px; width: 664px; height: 78px;
    background: var(--band-grey);
  }
  .contact-band__phone {
    position: absolute; left: 26px; top: 18px;
    font-size: 38px; font-weight: 700; color: #fff; letter-spacing: .5px;
  }
  .contact-band__details {
    position: absolute; right: 22px; top: 38px;
    font-size: 14px; line-height: 1.35; color: var(--ink); text-align: right;
  }
  .hero-photo {
    position: absolute; left: 340px; top: 0; width: 324px; height: 250px;
    background: linear-gradient(160deg, var(--sky-top), var(--sky-bottom) 70%, #e8d7b8);
  }
  .prices {
    position: absolute; left: 24px; top: 312px; width: 616px;
    display: grid; grid-template-columns: 1fr 1fr; column-gap: 28px;
  }
  .price-list { list-style: none; }
  .price-item {
    display: flex; justify-content: space-between; align-items: baseline;
    font-size: 15px; line-height: 1.3; margin-bottom: 3px;
  }
  .price-item__price { font-weight: 700; white-space: nowrap; margin-left: 8px; }
  .price-item__unit { font-size: 11px; font-weight: 400; }
  .price-item__note {
    display: block; font-size: 11px; color: var(--muted); line-height: 1.2;
  }
  .face-photo {
    position: absolute; left: 0; top: 560px; width: 362px; height: 380px;
    background: radial-gradient(ellipse at 50% 45%, var(--skin-light), var(--skin-mid) 60%, #fff 95%);
  }
  .hours-panel {
    position: absolute; left: 362px; top: 540px; width: 302px; height: 400px;
    background: var(--band-grey); padding: 20px 22px 0;
    color: #fff;
  }
  .hours-panel__title {
    text-align: center; font-size: 20px; font-weight: 400; letter-spacing: .5px;
    margin-bottom: 12px;
  }
  .hours-list { list-style: none; font-size: 14px; }
  .hours-row { display: flex; align-items: baseline; line-height: 1.45; }
  .hours-row__dots { flex: 1; border-bottom: 1px dotted #fff; margin: 0 4px; transform: translateY(-4px); }
  .hours-note { font-size: 11px; line-height: 1.3; }
  .location-map {
    position: absolute; left: 14px; bottom: 22px; width: 274px; height: 110px;
    background: linear-gradient(135deg, var(--map-light), var(--map-mid));
  }
</style>
</head>
<body>
<main class="flyer">
  <header class="brand">
    <span class="brand__initials">HVM</span>
    <span class="brand__name">HOLLY VANMERE<br>AESTHETICS</span>
    <span class="brand__web">www.hollyvanmereaesthetics.co.uk</span>
  </header>

  <div class="hero-photo" role="img" aria-label="Photo of a woman in sunglasses against a blue summer sky"></div>

  <section class="contact-band">
    <span class="contact-band__phone">0208 947 2186</span>
    <address class="contact-band__details" style="font-style:normal">
      hvmwarnfordbookings@mailbox.co.uk<br>
      6 Warnford Parade, Surrey, KT4 3JQ
    </address>
  </section>

  <section class="prices">
    <ul class="price-list">
      <li class="price-item"><span>Relaxon 1 area</span><span class="price-item__price">£100</span></li>
      <li class="price-item"><span>Relaxon 2 areas</span><span class="price-item__price">£150</span></li>
      <li class="price-item"><span>Relaxon 3 areas</span><span class="price-item__price">£200</span></li>
      <li class="price-item"><span>Lip Enhancement 0.5ml</span><span class="price-item__price">£100</span></li>
      <li class="price-item"><span>Lip Enhancement 1ml</span><span class="price-item__price">£200</span></li>
      <li class="price-item"><span>Facial Fillers</span><span class="price-item__price">£200 <span class="price-item__unit">per 1ml</span></span></li>
      <li class="price-item"><span>Volumiq<span class="price-item__note">(2 vials - must be bought as a course)</span></span><span class="price-item__price">£450 <span class="price-item__unit">per session</span></span></li>
      <li class="price-item"><span>Non Surgical Face Lift (Thread Lift)</span><span class="price-item__price">£600 <span class="price-item__unit">per area</span></span></li>
      <li class="price-item"><span>Skin Press Full Face</span><span class="price-item__price">£250</span></li>
    </ul>
    <ul class="price-list">
      <li class="price-item"><span>Skin Press Small Per Small Area</span><span class="price-item__price">£100</span></li>
      <li class="price-item"><span>Cryo Therapy</span><span class="price-item__price">£60</span></li>
      <li class="price-item"><span>Chemical Peel Light Peel<br>and Microdermabrasion</span><span class="price-item__price">£85</span></li>
      <li class="price-item"><span>Chemical Peel Deep Peel</span><span class="price-item__price">£150</span></li>
      <li class="price-item"><span>Consultation<span class="price-item__note">redeemable against service</span></span><span class="price-item__price">£30</span></li>
      <li class="price-item"><span>Relaxon Top Up Relaxon<span class="price-item__note">(must be within 2 weeks of 1st treatment)</span></span><span class="price-item__price">£50</span></li>
      <li class="price-item"><span>Filler Top Up<span class="price-item__note">(must be within 2 weeks of 1st appointment)</span></span><span class="price-item__price">£100</span></li>
    </ul>
  </section>

  <div class="face-photo" role="img" aria-label="Beauty portrait of a smiling woman with hands at her temples"></div>

  <section class="hours-panel">
    <h2 class="hours-panel__title">OPENING TIMES</h2>
    <ul class="hours-list">
      <li class="hours-row"><span>Monday</span><span class="hours-row__dots"></span><span>10am-4pm</span></li>
      <li class="hours-row"><span>Tuesday</span><span class="hours-row__dots"></span><span>10am-4pm</span></li>
      <li class="hours-row"><span>Wednesday</span><span class="hours-row__dots"></span><span>12pm-8pm</span></li>
      <li class="hours-row"><span>Thursday</span><span class="hours-row__dots"></span><span>7:30am-4:30pm</span></li>
      <li class="hours-note">(at number 1 Linwood Street only)</li>
      <li class="hours-row"><span>Friday</span><span class="hours-row__dots"></span><span>10am-2pm</span></li>
      <li class="hours-row"><span>Saturday</span><span class="hours-row__dots"></span><span>9am-2pm</span></li>
      <li class="hours-row"><span>Sunday</span><span class="hours-row__dots"></span><span>Closed</span></li>
    </ul>
    <div class="location-map" role="img" aria-label="Street map showing the clinic location on Warnford Parade"></div>
  </section>
</main>
</body>
</html>
```